QuillMark Business Cards

I need a business card designed for QuillMark. To get an idea of what we do please visit https://formvault.example/para-creadores-3

```html
<!DOCTYPE html>
<html lang="en">
<head>
<meta charset="utf-8">
<title>QuillMark Business Cards</title>
<link href="https://fonts.googleapis.com/css2?family=Poppins:wght@300;400;600&display=swap" rel="stylesheet">
<style>
  :root {
    --backdrop: #dcdcdc;
    --card-dark: #0c0e13;
    --card-orange: #e8900f;
    --accent: #f0961a;
    --ink-light: #f4f4f4;
    --ink-dark: #1a1a1a;
    --rule-dark: #4a4a4a;
  }
  * { margin: 0; padding: 0; box-sizing: border-box; }
  html, body { width: 1200px; height: 800px; overflow: hidden; }
  body {
    background: var(--backdrop);
    font-family: "Poppins", sans-serif;
    position: relative;
  }
  .card {
    position: absolute;
    top: 250px;
    width: 520px;
    height: 300px;
    border-radius: 18px;
    overflow: hidden;
  }
  .card--back { left: 50px; background: var(--card-dark); color: var(--ink-light); }
  .card--front { left: 630px; background: var(--card-orange); color: var(--ink-dark); }

  .wordmark {
    position: absolute;
    display: flex;
    align-items: center;
    gap: 14px;
    font-weight: 300;
    text-transform: uppercase;
  }
  .wordmark__square { border: 1.5px solid currentColor; }
  .card--back .wordmark { top: 62px; left: 172px; font-size: 22px; letter-spacing: 7px; color: var(--ink-light); }
  .card--back .wordmark__square { width: 30px; height: 30px; border-color: var(--accent); }
  .card--front .wordmark { top: 118px; left: 92px; font-size: 32px; letter-spacing: 10px; }
  .card--front .wordmark__square { width: 48px; height: 48px; }

  .divider {
    position: absolute;
    left: 40px; right: 40px; top: 150px;
    height: 1px;
    background: var(--accent);
  }
  .person { position: absolute; left: 40px; top: 172px; }
  .person__name { color: var(--accent); font-weight: 600; font-size: 18px; line-height: 1.1; text-transform: uppercase; }
  .person__title { font-size: 12px; font-weight: 400; margin-top: 2px; }
  .person__rule { width: 130px; height: 1px; background: var(--accent); margin: 8px 0 6px; }
  .contact-list { list-style: none; font-size: 12px; line-height: 1.55; }
  .contact-list li { display: flex; align-items: center; gap: 8px; }
  .contact-list svg { width: 11px; height: 11px; fill: var(--accent); flex: none; }

  .address {
    position: absolute;
    right: 40px; top: 176px;
    text-align: right;
    font-size: 12px;
    line-height: 1.5;
  }
  .address__web { color: var(--accent); }
</style>
</head>
<body>

<section class="card card--back" aria-label="Card back with contact details">
  <div class="wordmark"><span class="wordmark__square"></span><span class="wordmark__name">QuillMark</span></div>
  <div class="divider"></div>

  <div class="person">
    <p class="person__name">Daniel Reyes</p>
    <p class="person__title">President</p>
    <div class="person__rule"></div>
    <ul class="contact-list">
      <li><svg viewBox="0 0 16 16"><path d="M3 1h3l1.5 4-2 1.5a9 9 0 0 0 4 4L11 8.5 15 10v3a2 2 0 0 1-2 2A12 12 0 0 1 1 3a2 2 0 0 1 2-2z"/></svg>555-014-2231</li>
      <li><svg viewBox="0 0 16 16"><path d="M4 0h8a1 1 0 0 1 1 1v14a1 1 0 0 1-1 1H4a1 1 0 0 1-1-1V1a1 1 0 0 1 1-1zm1 2v10h6V2zm3 11a1 1 0 1 0 0 2 1 1 0 0 0 0-2z"/></svg>555-014-7760</li>
      <li><svg viewBox="0 0 16 16"><path d="M4 0h8v4H4zM1 5h14v8h-3v3H4v-3H1zm5 6v3h4v-3z"/></svg>555-014-3398</li>
      <li><svg viewBox="0 0 16 16"><path d="M0 3h16v10H0zm1.5 1.2v.4L8 9l6.5-4.4v-.4z"/></svg>reyes@quillmark.example</li>
    </ul>
  </div>

  <address class="address" style="font-style:normal">
    QuillMark Digital Notary<br>
    142 Birchwood Court<br>
    Juneau, Alaska 99801<br>
    <span class="address__web">www.quillmark.example</span>
  </address>
</section>

<section class="card card--front" aria-label="Card front with company name">
  <div class="wordmark"><span class="wordmark__square"></span><span class="wordmark__name">QuillMark</span></div>
</section>

</body>
</html>
```